MOLT - Monitoring Natural Hazards from Space Web Application

KORVEN Sarl is a Luxembourg based Space-Startup that works in the field of Earth Observation. KORVEN is a platform able to extract value-added information from satellite data and is specialized in mapping Natural Disaster (floods, fires etc).

We are now developing a new vertical tool, called MOLT, dedicated to the monitoring of natural hazards in Humanitarian Camps around the world.

The goal of MOLT is to hide to the users' all the complexity of the Satellite Image processing and just provide them the results.

This project require to Design 4 pages of MOLT:
• Public Home Page (Code - V01)
• Dashboard (private Home Page) (Code - V03)
• Monitor (web GIS) (Code - V14)
• Registration Page (Code - V04)

We would like to provide the required time to make a good job.

Target Market(s)

Humanitarian Agencies, Goverments

Coding

Coded - Design and coding required

Number of Pages Required

4 page

Font styles to use
Other font styles liked:
• see the manual attached

Requirements
Must have
• 4 pages. One Home, one form, one dashboard and one web map.
Nice to have
• Please read the attachment with all the detailed instructions

```html
<!DOCTYPE html>
<html lang="en">
<head>
<meta charset="utf-8">
<title>MOLT Monitor</title>
<link href="https://fonts.googleapis.com/css2?family=Figtree:wght@400;500;600;700&display=swap" rel="stylesheet">
<style>
:root{
  --sidebar-top:#18262e;
  --sidebar-bottom:#2f5560;
  --accent:#f0bd38;
  --teal:#264b59;
  --pin:#2c4a55;
  --panel:#f1f1f1;
  --card:#ffffff;
  --ink:#1e1e1e;
  --muted:#555b60;
  --line:#d9dcde;
  --map-a:#e2e2e2;
  --map-b:#cfcfcf;
}
*{box-sizing:border-box;margin:0;padding:0}
html,body{width:1200px;height:752px;overflow:hidden}
body{font-family:"Figtree",Arial,sans-serif;color:var(--ink);background:#fff;position:relative}
.sidebar{position:absolute;left:0;top:0;width:223px;height:752px;background:linear-gradient(180deg,var(--sidebar-top) 0%,#1f3843 50%,var(--sidebar-bottom) 100%);color:#fff}
.brand{position:absolute;left:22px;top:40px;display:flex;align-items:center;gap:10px}
.brand-dot{width:30px;height:30px;border:2px solid #fff;border-radius:50%}
.brand-name{font-size:24px;font-weight:500;letter-spacing:5px}
.divider{position:absolute;left:20px;width:190px;height:1px;background:rgba(255,255,255,.18)}
.user{position:absolute;left:29px;top:123px;display:flex;align-items:center;gap:11px}
.avatar{width:36px;height:36px;border-radius:50%;background:linear-gradient(135deg,#f3e2d0,#e8b83a);position:relative}
.avatar::after{content:"";position:absolute;right:-1px;bottom:1px;width:8px;height:8px;border-radius:50%;background:#3ec25a;border:1.5px solid var(--sidebar-top)}
.user-name{font-size:12.5px;font-weight:600}
.user-mail{font-size:9px;opacity:.75}
.user-caret{position:absolute;left:187px;top:133px}
.nav-item{position:absolute;left:16px;width:195px;height:38px;display:flex;align-items:center;gap:14px;padding-left:13px;font-size:14.5px;font-weight:600}
.nav-item.active{background:var(--accent);color:var(--teal);box-shadow:0 8px 14px rgba(0,0,0,.25)}
.nav-item.signout{color:var(--accent);font-weight:500}
.nav-item.setting{font-weight:500}
.topbar{position:absolute;left:223px;top:0;width:977px;height:46px;background:#fff;box-shadow:0 1px 4px rgba(0,0,0,.05);z-index:2}
.top-search{position:absolute;left:222px;top:12px;width:347px;height:23px;border-radius:12px;background:#ececec}
.top-search svg{position:absolute;right:12px;top:6px}
.top-links{position:absolute;left:585px;top:15px;display:flex;align-items:center;font-size:10px;font-weight:500;white-space:nowrap}
.top-link{display:flex;align-items:center;gap:6px;padding:0 12px;border-left:1px solid var(--line)}
.panel{position:absolute;left:223px;top:46px;width:290px;height:706px;background:var(--panel)}
.layer-search{position:absolute;left:14px;top:29px;width:195px;height:37px;background:#fff;font-size:11.5px;color:#9a9a9a;padding:12px 18px}
.filter-btn{position:absolute;left:220px;top:29px;width:53px;height:37px;background:var(--teal);border-radius:3px;display:flex;align-items:center;justify-content:center}
.layers-title{position:absolute;left:30px;top:96px;font-size:13px;font-weight:500}
.layer-card{position:absolute;left:14px;width:259px;height:52px;background:var(--card);border-radius:6px;display:flex;align-items:center;gap:14px;padding-left:16px;font-size:15px;font-weight:500}
.layer-card.active{border-left:2px solid var(--accent);box-shadow:0 4px 10px rgba(0,0,0,.1)}
.more-btn{position:absolute;left:14px;top:451px;width:259px;height:52px;background:var(--teal);border-radius:6px;color:#fff;display:flex;align-items:center;justify-content:center;gap:10px;font-size:15px;font-weight:500}
.main{position:absolute;left:513px;top:46px;width:687px;height:706px}
.page-title{position:absolute;left:37px;top:23px;font-size:26px;font-weight:700}
.map{position:absolute;left:22px;top:77px;width:643px;height:454px;border-radius:17px;background:linear-gradient(135deg,var(--map-a),var(--map-b));overflow:hidden}
.map-focus{position:absolute;left:225px;top:102px;width:94px;height:94px;border-radius:50%;background:rgba(120,130,135,.22);border:1px solid rgba(80,90,95,.45)}
.pin{position:absolute;width:22px;height:30px;margin:-11px 0 0 -11px}
.map-btn{position:absolute;width:29px;height:29px;border-radius:50%;background:#4f5457;display:flex;align-items:center;justify-content:center}
.map-tools{position:absolute;left:250px;top:22px;width:143px;height:29px;border-radius:15px;background:#fff;display:flex;align-items:center;justify-content:space-around;padding:0 6px}
.zoom{position:absolute;left:598px;top:389px;width:27px;height:48px;border-radius:8px;background:#4f5457;display:flex;flex-direction:column;align-items:center;justify-content:space-around;color:#fff;font-size:15px;font-weight:600}
.timeline-title{position:absolute;left:36px;top:550px;font-size:13.5px;font-weight:500}
.timeline-text{position:absolute;left:36px;width:610px;font-size:11px;line-height:18px;color:var(--muted)}
</style>
</head>
<body>
<aside class="sidebar">
  <div class="brand"><span class="brand-dot"></span><span class="brand-name">MOLT</span></div>
  <div class="divider" style="top:108px"></div>
  <div class="user">
    <div class="avatar" role="img" aria-label="User profile photo"></div>
    <div><div class="user-name">Lena Marwick</div><div class="user-mail">lenamarwick@postbay.com</div></div>
  </div>
  <svg class="user-caret" width="8" height="6" viewBox="0 0 8 6"><path d="M1 1l3 3 3-3" stroke="#fff" stroke-width="1.4" fill="none"/></svg>
  <div class="divider" style="top:173px"></div>
  <div class="nav-item" style="top:202px">
    <svg width="13" height="13" viewBox="0 0 14 14"><path d="M2 7l5-5 5 5v6H2z" fill="none" stroke="#fff" stroke-width="1.3"/></svg>Dashboard</div>
  <div class="nav-item active" style="top:258px">
    <svg width="14" height="13" viewBox="0 0 14 13"><rect x="1" y="1" width="12" height="8" fill="none" stroke="#264b59" stroke-width="1.3"/><path d="M3 6h2l1-2 2 3 1-1h2M5 12h4" stroke="#264b59" stroke-width="1.2" fill="none"/></svg>Monitor</div>
  <div class="nav-item setting" style="top:626px">
    <svg width="15" height="15" viewBox="0 0 16 16"><circle cx="8" cy="8" r="2.5" fill="none" stroke="#fff" stroke-width="1.3"/><circle cx="8" cy="8" r="6" fill="none" stroke="#fff" stroke-width="1.3" stroke-dasharray="3 1.5"/></svg>Setting</div>
  <div class="nav-item signout" style="top:674px">
    <svg width="15" height="15" viewBox="0 0 16 16"><path d="M9 2H3v12h6M7 8h8M12 5l3 3-3 3" fill="none" stroke="#f0bd38" stroke-width="1.4"/></svg>Sign Out</div>
</aside>

<header class="topbar">
  <div class="top-search"><svg width="11" height="11" viewBox="0 0 12 12"><circle cx="5" cy="5" r="3.8" fill="none" stroke="#888" stroke-width="1.2"/><path d="M8 8l3 3" stroke="#888" stroke-width="1.2"/></svg></div>
  <nav class="top-links">
    <div class="top-link"><svg width="17" height="17" viewBox="0 0 18 18"><circle cx="9" cy="9" r="7.5" fill="none" stroke="#222" stroke-width="1.3"/><circle cx="6" cy="7" r="1.2"/><circle cx="10" cy="5.5" r="1.2"/><circle cx="12.5" cy="9" r="1.2"/></svg>THEME</div>
    <div class="top-link"><svg width="17" height="17" viewBox="0 0 18 18"><rect x="1.5" y="2" width="14" height="14" rx="3" fill="none" stroke="#222" stroke-width="1.3"/><path d="M4 12l3-4 3 2 4-5" fill="none" stroke="#222" stroke-width="1.3"/></svg>ACTIVITY</div>
    <div class="top-link"><svg width="17" height="17" viewBox="0 0 18 18"><circle cx="9" cy="9" r="7.5" fill="none" stroke="#222" stroke-width="1.3"/><path d="M7 7a2 2 0 1 1 2 2v2" fill="none" stroke="#222" stroke-width="1.3"/><circle cx="9" cy="13" r=".9"/></svg>HELP CENTER</div>
    <div class="top-link"><svg width="19" height="17" viewBox="0 0 20 18"><rect x="1" y="1" width="10" height="9" rx="1.5" fill="none" stroke="#222" stroke-width="1.3"/><rect x="8" y="7" width="10" height="9" rx="1.5" fill="#fff" stroke="#222" stroke-width="1.3"/></svg>ENG
      <svg width="7" height="5" viewBox="0 0 8 6"><path d="M1 1l3 3 3-3" stroke="#222" stroke-width="1.4" fill="none"/></svg></div>
  </nav>
</header>

<section class="panel">
  <div class="layer-search">Searh Here...</div>
  <div class="filter-btn"><svg width="18" height="16" viewBox="0 0 18 16"><path d="M1 3h16M1 8h16M1 13h16" stroke="#fff" stroke-width="1.3"/><circle cx="11" cy="3" r="2" fill="#264b59" stroke="#fff" stroke-width="1.3"/><circle cx="6" cy="8" r="2" fill="#264b59" stroke="#fff" stroke-width="1.3"/><circle cx="11" cy="13" r="2" fill="#264b59" stroke="#fff" stroke-width="1.3"/></svg></div>
  <div class="layers-title">Pre-defined Layers :</div>
  <div class="layer-card" style="top:127px"><svg width="30" height="22" viewBox="0 0 30 22"><path d="M4 12l8-7 8 7M8 9v6h8V9M1 17c3-2 5 2 8 0s5 2 8 0 5 2 8 0 4 1 4 1" fill="none" stroke="#222" stroke-width="1.2"/></svg>Flooded Areas</div>
  <div class="layer-card" style="top:189px"><svg width="30" height="26" viewBox="0 0 30 26"><rect x="9" y="2" width="12" height="22" fill="none" stroke="#222" stroke-width="1.2"/><path d="M12 6h2M16 6h2M12 10h2M16 10h2M12 14h2M16 14h2M12 18h2M16 18h2M5 24h20" stroke="#222" stroke-width="1.2"/></svg>Buildings</div>
  <div class="layer-card active" style="top:251px"><svg width="30" height="26" viewBox="0 0 30 26"><path d="M15 14V6M15 9c-4-1-5-5-5-5s5 0 5 4M15 8c3-2 6-1 6-1s-2 4-6 3M3 18l5-2h8c2 0 2 3 0 3h-5M8 24l4-3h10l5-5" fill="none" stroke="#222" stroke-width="1.2"/></svg>Impacts</div>
  <div class="layer-card" style="top:316px"><svg width="30" height="26" viewBox="0 0 30 26"><circle cx="15" cy="7" r="5" fill="none" stroke="#222" stroke-width="1.2"/><path d="M13 9l4-4M4 24h22M6 24v-7h5v7M12 24v-10h6v10M19 24v-7h5v7" fill="none" stroke="#222" stroke-width="1.2"/></svg>Drought Index</div>
  <div class="layer-card" style="top:381px"><svg width="30" height="26" viewBox="0 0 30 26"><rect x="2" y="3" width="26" height="16" fill="none" stroke="#222" stroke-width="1.2"/><path d="M5 12h5l2-5 3 9 2-4h8M11 23h8M15 19v4" fill="none" stroke="#222" stroke-width="1.2"/></svg>Monitoring Stations</div>
  <div class="more-btn"><svg width="18" height="18" viewBox="0 0 18 18"><circle cx="9" cy="9" r="8" fill="none" stroke="#fff" stroke-width="1.3"/><path d="M9 5v8M5 9h8" stroke="#fff" stroke-width="1.3"/></svg>Search More Layers</div>
</section>

<main class="main">
  <h1 class="page-title">MOLT Monitor</h1>
  <div class="map" role="img" aria-label="World map of Europe, Africa and Asia with camp location pins">
    <div class="map-focus"></div>
    <svg class="pin" style="left:580px;top:57px" viewBox="0 0 22 30"><path d="M11 1C5.5 1 1 5.3 1 10.8 1 18 11 29 11 29s10-11 10-18.2C21 5.3 16.5 1 11 1z" fill="var(--pin)"/><circle cx="11" cy="10.5" r="4.3" fill="#fff"/></svg>
    <svg class="pin" style="left:419px;top:124px" viewBox="0 0 22 30"><path d="M11 1C5.5 1 1 5.3 1 10.8 1 18 11 29 11 29s10-11 10-18.2C21 5.3 16.5 1 11 1z" fill="var(--pin)"/><circle cx="11" cy="10.5" r="4.3" fill="#fff"/></svg>
    <svg class="pin" style="left:273px;top:148px" viewBox="0 0 22 30"><path d="M11 1C5.5 1 1 5.3 1 10.8 1 18 11 29 11 29s10-11 10-18.2C21 5.3 16.5 1 11 1z" fill="var(--pin)"/><circle cx="11" cy="10.5" r="4.3" fill="#fff"/></svg>
    <svg class="pin" style="left:111px;top:242px" viewBox="0 0 22 30"><path d="M11 1C5.5 1 1 5.3 1 10.8 1 18 11 29 11 29s10-11 10-18.2C21 5.3 16.5 1 11 1z" fill="var(--pin)"/><circle cx="11" cy="10.5" r="4.3" fill="#fff"/></svg>
    <svg class="pin" style="left:490px;top:257px" viewBox="0 0 22 30"><path d="M11 1C5.5 1 1 5.3 1 10.8 1 18 11 29 11 29s10-11 10-18.2C21 5.3 16.5 1 11 1z" fill="var(--pin)"/><circle cx="11" cy="10.5" r="4.3" fill="#fff"/></svg>
    <svg class="pin" style="left:366px;top:295px" viewBox="0 0 22 30"><path d="M11 1C5.5 1 1 5.3 1 10.8 1 18 11 29 11 29s10-11 10-18.2C21 5.3 16.5 1 11 1z" fill="var(--pin)"/><circle cx="11" cy="10.5" r="4.3" fill="#fff"/></svg>
    <svg class="pin" style="left:276px;top:388px" viewBox="0 0 22 30"><path d="M11 1C5.5 1 1 5.3 1 10.8 1 18 11 29 11 29s10-11 10-18.2C21 5.3 16.5 1 11 1z" fill="var(--pin)"/><circle cx="11" cy="10.5" r="4.3" fill="#fff"/></svg>
    <div class="map-btn" style="left:14px;top:14px"><svg width="13" height="13" viewBox="0 0 14 14"><path d="M1 5V1h4M9 1h4v4M13 9v4H9M5 13H1V9" fill="none" stroke="#fff" stroke-width="1.4"/></svg></div>
    <div class="map-tools">
      <svg width="14" height="12" viewBox="0 0 14 12"><path d="M1 7l6-5 6 5M3 6v5h8V6" fill="none" stroke="#264b59" stroke-width="1.4"/></svg>
      <svg width="12" height="14" viewBox="0 0 12 14"><rect x="2" y="1" width="8" height="12" fill="none" stroke="#264b59" stroke-width="1.4"/><path d="M4 4h4M4 7h4M4 10h4" stroke="#264b59" stroke-width="1.2"/></svg>
      <svg width="18" height="14" viewBox="0 0 18 14"><path d="M2 13h14M4 13V8M9 13V4M14 13V7M3 6l5-4 4 3 5-3" fill="none" stroke="#264b59" stroke-width="1.4"/></svg>
      <svg width="16" height="16" viewBox="0 0 16 16"><circle cx="8" cy="8" r="7" fill="none" stroke="#264b59" stroke-width="1.3"/><circle cx="5" cy="8" r="1" fill="#264b59"/><circle cx="8" cy="8" r="1" fill="#264b59"/><circle cx="11" cy="8" r="1" fill="#264b59"/></svg>
    </div>
    <div class="map-btn" style="left:14px;top:333px"><svg width="11" height="11" viewBox="0 0 12 12"><circle cx="5" cy="5" r="3.8" fill="none" stroke="#fff" stroke-width="1.3"/><path d="M8 8l3 3" stroke="#fff" stroke-width="1.3"/></svg></div>
    <div class="map-btn" style="left:14px;top:369px"><svg width="13" height="13" viewBox="0 0 14 14"><rect x="1" y="1" width="12" height="12" rx="2" fill="none" stroke="#fff" stroke-width="1.3"/><path d="M5 9l5-5M6 4h4v4" fill="none" stroke="#fff" stroke-width="1.3"/></svg></div>
    <div class="map-btn" style="left:14px;top:404px"><svg width="13" height="13" viewBox="0 0 14 14"><path d="M7 2H2v10h10V7M6 8l6-6 1 1-6 6H6z" fill="none" stroke="#fff" stroke-width="1.3"/></svg></div>
    <div class="map-btn" style="left:598px;top:356px;width:26px;height:26px"><svg width="11" height="11" viewBox="0 0 12 12"><rect x="1" y="3" width="8" height="8" fill="none" stroke="#fff" stroke-width="1.3"/><path d="M3 1h8v8" fill="none" stroke="#fff" stroke-width="1.3"/></svg></div>
    <div class="zoom"><span>+</span><span>−</span></div>
  </div>
  <div class="timeline-title">Timeline :</div>
  <p class="timeline-text" style="top:577px">This component must show a temporal time line that can be zoomed in or out. The user should be able to browse the time that will go from a range up to 10/20 years. But the control should be able to zoom in up to see day by day.</p>
  <p class="timeline-text" style="top:629px">In some dates (the days where we detect for example a flood) there will be some icons to let the user understand that something happened that day(s)</p>
</main>
</body>
</html>
```